Business Cards for Tomas and Welby

Design of business cards for two people with the recently created brand Caldor Mobile. Caldor Mobile wants to become a worldwide major player on the secondhand phone market. It gathers send hand phones from individuals, refurbish them and sell them throughout the world. It has a green impact (recycling) and we also contribute to social project in Africa (a percentage of our benefits are sent to build school, sport facilities, etc.

Target Market(s)

B2B - Tomas and Welby are in contact with distributors across Africa.

Industry/Entity Type

Wireless Communication

Contact Information for Business Card

Tomas Vireaux
Head of Emerging Markets
Caldor Energy South Africa (Pty) Ltd
Fennick Street 47
2031 Sandton - Johannesburg
South Africa
Tel: + 27 10 555 0184
Mobile : +27 82 55 017
Email : tomas.vireaux@caldormobile.example
Skype: tomas.vireaux
Web: www.caldormobile.example
 

Welby Crofts
Head of Southern Africa
Fennick Street 47
South Africa
Tel: + 27 10 555 0184
Mobile: +27 83 555 0297
Email: welby.crofts@caldormobile.example
Skype: welby.crofts
Web: www.caldormobile.example

Requirements
Must have
• The cards need to be "serious", trustable, with a worldwide presence.
Nice to have
• Some "green" / recycling touch would be nice but not necessary if in contradiction with the general design.

```html
<!DOCTYPE html>
<html lang="en">
<head>
<meta charset="utf-8">
<title>Caldor Mobile – Business Card</title>
<link rel="stylesheet" href="https://fonts.googleapis.com/css2?family=Open+Sans:wght@400;600;700&display=swap">
<style>
  :root {
    --backdrop: #4a413c;
    --card: #151617;
    --card-edge: #0c0d0e;
    --brand-blue: #2a86c8;
    --brand-blue-deep: #246fa6;
    --text-light: #f2f2f2;
    --text-muted: #8d8f92;
    --rule: #e6e6e6;
  }
  * { box-sizing: border-box; margin: 0; padding: 0; }
  html, body {
    width: 1200px; height: 864px; overflow: hidden;
    background: var(--backdrop);
    font-family: "Open Sans", Arial, sans-serif;
  }
  .canvas {
    width: 1200px; height: 864px;
    display: flex; align-items: center; justify-content: center; gap: 50px;
  }
  .card {
    position: relative;
    width: 540px; height: 336px;
    background: var(--card);
    border-radius: 3px;
    box-shadow: 0 2px 0 var(--card-edge), 0 18px 40px rgba(0,0,0,.45);
    overflow: hidden;
  }

  /* Front */
  .card-front {
    display: flex; flex-direction: column; align-items: center; justify-content: center;
  }
  .brand-mark {
    display: flex; align-items: center; gap: 14px;
    color: var(--brand-blue);
    font-weight: 700; font-size: 40px; letter-spacing: .5px;
  }
  .brand-mark .brand-dot {
    width: 22px; height: 22px; border-radius: 50%;
    background: var(--brand-blue);
  }
  .front-web {
    margin-top: 44px;
    color: var(--text-muted);
    font-size: 15px; letter-spacing: 6px;
  }

  /* Back */
  .person {
    position: absolute; left: 30px; top: 40px;
  }
  .person-name {
    color: var(--brand-blue-deep);
    font-weight: 700; font-size: 19px; text-transform: uppercase; letter-spacing: .3px;
  }
  .person-title {
    color: var(--brand-blue);
    font-size: 15px; margin-top: 1px;
  }
  .back-brand {
    position: absolute; right: 30px; top: 72px;
    display: flex; align-items: center; gap: 10px;
    color: var(--brand-blue-deep);
    font-weight: 700; font-size: 24px;
  }
  .back-brand .brand-dot {
    width: 14px; height: 14px; border-radius: 50%;
    background: var(--brand-blue-deep);
  }
  .divider {
    position: absolute; left: 0; right: 0; top: 120px;
    height: 1.5px; background: var(--rule);
  }
  .contacts {
    position: absolute; left: 30px; top: 136px;
    list-style: none;
    color: var(--text-light); font-size: 13px; line-height: 20px;
  }
  .contacts li { display: flex; align-items: center; gap: 9px; white-space: nowrap; }
  .contacts svg { width: 12px; height: 12px; flex: none; fill: none; stroke: var(--text-light); stroke-width: 1.6; }
  .contacts .icon-dot { width: 10px; height: 10px; margin: 0 1px; border-radius: 50%; border: 1.6px solid var(--text-light); flex: none; }
  .address {
    position: absolute; right: 30px; top: 226px;
    font-style: normal; text-align: right; white-space: nowrap;
    color: var(--text-light); font-size: 15px; line-height: 22px;
  }
</style>
</head>
<body>
<main class="canvas">

  <section class="card card-front" aria-label="Card front">
    <div class="brand-mark"><span class="brand-dot"></span>Caldor Mobile</div>
    <p class="front-web">www.caldormobile.example</p>
  </section>

  <section class="card card-back" aria-label="Card back">
    <header class="person">
      <h1 class="person-name">Tomas Vireaux</h1>
      <p class="person-title">Head of Emerging Markets</p>
    </header>

    <div class="back-brand"><span class="brand-dot"></span>Caldor Mobile</div>

    <div class="divider"></div>

    <ul class="contacts">
      <li>
        <svg viewBox="0 0 12 12" aria-hidden="true"><path d="M2 1.5h2.2l1 2.6-1.3 1a6 6 0 0 0 3 3l1-1.3 2.6 1V10a1 1 0 0 1-1 1A9 9 0 0 1 1 2.5a1 1 0 0 1 1-1z"/></svg>
        + 27 10 555 0184
      </li>
      <li>
        <svg viewBox="0 0 12 12" aria-hidden="true"><rect x="3" y="1" width="6" height="10" rx="1"/><path d="M5.3 9.2h1.4"/></svg>
        +27 82 55 017
      </li>
      <li>
        <svg viewBox="0 0 12 12" aria-hidden="true"><rect x="1" y="2.5" width="10" height="7" rx=".8"/><path d="M1.3 3l4.7 3.6L10.7 3"/></svg>
        tomas.vireaux@caldormobile.example
      </li>
      <li>
        <span class="icon-dot" aria-hidden="true"></span>
        tomas.vireaux
      </li>
    </ul>

    <address class="address">
      Caldor Energy South Africa (Pty) Ltd<br>
      Fennick Street 47<br>
      2031 Sandton - Johannesburg<br>
      South Africa
    </address>
  </section>

</main>
</body>
</html>
```